Ebook sucht Cover
Zielgruppe
Wir betreiben diverse Internetprojekte- und -portale aller Themen und Branchen.
Aufgabenstellung
Wir haben im März 2014 ein Ebook über die Investitionsmöglichkeiten im Irak erarbeitet, welches derzeit auf aktuellen von Herbst 2015 Stand gebracht und überarbeitet wird. Vor Einfall der KV, war der Irak, vorrangig die Region Kurdistan, Erbil, ein sehr beliebtes Investitionsziel. Unser Ebook erzählt die Geschichte, Zahlen, Daten Fakten, aktuelle Situation sowie Zukunftsaussichten für ein Land (vor dem KV) mit einem des mit weltweit größten Wirtschaftswachstums.
Titel: Goldene Brücken - Traum oder Wende-Zeit
Format A4
kein Verlagslogo- und Autor auf Titelseite

```html
<!DOCTYPE html>
<html lang="de">
<head>
<meta charset="utf-8">
<title>Goldene Brücken – Traum oder Wende-Zeit</title>
<link rel="stylesheet" href="https://fonts.googleapis.com/css2?family=Carlito:ital,wght@1,700&family=Mulish:ital,wght@1,500&display=swap">
<style>
  :root {
    --sand-band: #d3bc91;
    --plaster-light: #e4d6b8;
    --plaster-mid: #d8c7a4;
    --stone-top: #c4b79f;
    --stone-bottom: #b9ab92;
    --title-white: #ffffff;
    --subtitle-gold: #c9a765;
    --shadow: rgba(40, 30, 15, 0.55);
  }
  html, body {
    margin: 0;
    padding: 0;
    overflow: hidden;
    background: #f3f0ea;
  }
  .cover {
    position: relative;
    width: 848px;
    height: 1200px;
    overflow: hidden;
    background: var(--sand-band);
  }
  .cover-backdrop {
    position: absolute;
    inset: 0;
    width: 848px;
    height: 1200px;
  }
  .title {
    position: absolute;
    left: 0;
    top: 0;
    margin: 0;
    font-family: "Carlito", "Calibri", sans-serif;
    font-style: italic;
    font-weight: 700;
    color: var(--title-white);
    text-shadow: 3px 4px 4px var(--shadow);
    line-height: 1;
  }
  .title-line {
    position: absolute;
    display: block;
    white-space: nowrap;
    font-size: 148px;
    letter-spacing: 1px;
  }
  .title-line--first { left: 74px; top: 214px; }
  .title-line--second { left: 56px; top: 372px; }
  .title-rule {
    position: absolute;
    left: 48px;
    top: 348px;
    width: 764px;
    height: 14px;
    background: linear-gradient(#ffffff, #ece8ea);
    box-shadow: 2px 4px 4px var(--shadow);
  }
  .subtitle {
    position: absolute;
    left: 0;
    width: 848px;
    top: 820px;
    margin: 0;
    font-family: "Mulish", "Century Gothic", sans-serif;
    font-style: italic;
    font-weight: 500;
    font-size: 100px;
    line-height: 128px;
    color: var(--subtitle-gold);
    text-align: center;
    text-shadow: 2px 3px 3px rgba(60, 45, 20, 0.5);
  }
  .subtitle-line { display: block; }
  .subtitle-line--first { padding-left: 20px; }
  .subtitle-line--second { padding-left: 0; }
</style>
</head>
<body>
  <main class="cover">
    <svg class="cover-backdrop" viewBox="0 0 848 1200" xmlns="http://www.w3.org/2000/svg">
      <defs>
        <linearGradient id="plaster-fill" x1="0" y1="0" x2="0" y2="1">
          <stop offset="0" stop-color="var(--plaster-light)"/>
          <stop offset="1" stop-color="var(--plaster-mid)"/>
        </linearGradient>
        <linearGradient id="stone-fill" x1="0" y1="0" x2="0" y2="1">
          <stop offset="0" stop-color="var(--stone-top)"/>
          <stop offset="1" stop-color="var(--stone-bottom)"/>
        </linearGradient>
      </defs>
      <path class="plaster-arc" role="img" aria-label="Heller, rauer Putz einer Lehmwand"
            d="M0,185 Q416,22 848,282 L848,1200 L0,1200 Z" fill="url(#plaster-fill)"/>
      <path class="stone-arch" role="img" aria-label="Alter Torbogen aus Bruchstein mit Schatten einer Person, in sandigen Grautönen"
            d="M0,562 Q516,147 848,836 L848,1200 L0,1200 Z" fill="url(#stone-fill)"/>
    </svg>

    <h1 class="title">
      <span class="title-line title-line--first">GOLDENE</span>
      <span class="title-line title-line--second">BRÜCKEN</span>
    </h1>
    <div class="title-rule" aria-hidden="true"></div>

    <p class="subtitle">
      <span class="subtitle-line subtitle-line--first">Traum oder</span>
      <span class="subtitle-line subtitle-line--second">Wende-Zeit</span>
    </p>
  </main>
</body>
</html>
```